Professional Home Buyer business card needed

I need a pretty straight forward business card designed. We help people that NEED to sell their homes solve problems. We perform all types of Real Estate transactions including flip, wholesale, investment, rental property and multi family. The card will mainly be used to give to prospective Sellers but will also be given to Real Estate Investors as well. It should professional and very easy to read, most clients are older people.

Target Market(s)

Distressed home sellers as well as Real Estate investors

Industry/Entity Type

Real Estate

Contact Information for Business Card

should be a professional layout

Colors
ec1f27
ffffff
000000

Requirements
Must have
• Large logo on back and smaller one on front. should utilize Red, white, and black.
• I am thinking of using a soft touch coating on the card so keep that in mind.
• Contact info should be very easy to read, think older clients.
Nice to have
• I would like to see a design with rounded corners on the card
Should not have
• pictures of homes or other home graphics.

```html
<!DOCTYPE html>
<html lang="en">
<head>
<meta charset="utf-8">
<title>Summit Home Buyers – Business Card</title>
<link href="https://fonts.googleapis.com/css2?family=Lato:wght@400;700&family=Saira:wght@700;800&display=swap" rel="stylesheet">
<style>
  :root {
    --red: #ec1f27;
    --white: #ffffff;
    --black: #000000;
    --ink: #1d1d1d;
    --card-dark: #262626;
    --backdrop: #e6e3df;
  }
  * { margin: 0; padding: 0; box-sizing: border-box; }
  html, body { width: 1200px; height: 1200px; overflow: hidden; }
  body { background: var(--backdrop); position: relative; font-family: "Lato", sans-serif; }

  .card {
    position: absolute;
    border-radius: 28px;
    box-shadow: 3px 4px 6px rgba(0,0,0,.35);
    overflow: hidden;
  }
  .card--front { left: 331px; top: 240px; width: 552px; height: 343px; background: var(--white); }
  .card--back  { left: 331px; top: 619px; width: 556px; height: 344px; background: var(--card-dark); }

  .tagline {
    position: absolute;
    font-family: "Saira", sans-serif;
    font-weight: 700;
    font-size: 11px;
    letter-spacing: 4px;
    white-space: nowrap;
  }
  .brand-name {
    position: absolute;
    font-family: "Saira", sans-serif;
    font-weight: 800;
    line-height: 1;
    display: flex;
    align-items: center;
    gap: 12px;
  }
  .brand-mark { display: inline-block; background: var(--red); }
  .brand-sub {
    position: absolute;
    font-family: "Saira", sans-serif;
    font-weight: 800;
    letter-spacing: 5px;
    white-space: nowrap;
  }

  /* Front */
  .card--front .tagline { left: 50px; top: 39px; color: var(--ink); }
  .card--front .brand-name { left: 40px; top: 62px; font-size: 56px; color: var(--black); }
  .card--front .brand-mark { width: 14px; height: 14px; }
  .card--front .brand-sub { left: 62px; top: 139px; font-size: 18px; color: var(--ink); }

  .person-name {
    position: absolute; left: 33px; top: 188px;
    font-family: "Saira", sans-serif; font-weight: 700;
    font-size: 23px; line-height: 28px; color: var(--red); letter-spacing: .3px;
  }
  .person-title { position: absolute; left: 33px; top: 216px; font-size: 19px; line-height: 23px; color: var(--ink); }

  .contact-list { position: absolute; left: 33px; top: 252px; list-style: none; }
  .contact-list li {
    display: flex; align-items: center; gap: 4px;
    font-size: 19px; color: var(--ink); line-height: 23px;
  }
  .contact-list svg { width: 14px; height: 14px; flex: none; }

  /* Back */
  .card--back .tagline { left: 0; right: 0; top: 120px; text-align: center; color: var(--white); }
  .card--back .brand-name { left: 0; right: 0; top: 150px; justify-content: center; font-size: 62px; color: var(--white); }
  .card--back .brand-mark { width: 16px; height: 16px; }
  .card--back .brand-sub { left: 0; right: 0; top: 238px; text-align: center; font-size: 21px; color: var(--white); letter-spacing: 6px; }
  .back-url { position: absolute; left: 0; right: 0; top: 288px; text-align: center; font-size: 18px; color: var(--red); }
</style>
</head>
<body>

<section class="card card--front" aria-label="Business card front">
  <p class="tagline">WE SOLVE HOME WORRIES!</p>
  <p class="brand-name"><span class="brand-mark" aria-hidden="true"></span>SUMMIT</p>
  <p class="brand-sub">HOME BUYERS</p>

  <h1 class="person-name">DANIEL HARTLEY</h1>
  <p class="person-title">President</p>

  <ul class="contact-list">
    <li>
      <svg viewBox="0 0 16 16" aria-hidden="true"><path fill="#ec1f27" d="M1 6c0-2 3-4 7-4s7 2 7 4v1h-3V5.5H4V7H1zM3 8h10l1 6H2zm5 1.5a2 2 0 1 0 0 4 2 2 0 0 0 0-4z"/></svg>
      316-555-0148
    </li>
    <li>
      <svg viewBox="0 0 16 16" aria-hidden="true"><rect x="1" y="3" width="14" height="10" fill="#ec1f27"/><path d="M1.5 3.5 8 9l6.5-5.5M1.5 12.5l5-4.5m8 4.5-5-4.5" stroke="#fff" stroke-width="1.2" fill="none"/></svg>
      dan@prairiehomesforcash.com
    </li>
    <li>
      <svg viewBox="0 0 16 16" aria-hidden="true"><circle cx="8" cy="8" r="7" fill="#ec1f27"/><path d="M5 4c2 0 2 2 4 2s0 3-2 3-1 3-2 3M11 10c1-1 2 0 2 1" stroke="#fff" stroke-width="1.4" fill="none"/></svg>
      www.prairiehomesforcash.com
    </li>
  </ul>
</section>

<section class="card card--back" aria-label="Business card back">
  <p class="tagline">WE SOLVE HOME WORRIES!</p>
  <p class="brand-name"><span class="brand-mark" aria-hidden="true"></span>SUMMIT</p>
  <p class="brand-sub">HOME BUYERS</p>
  <p class="back-url">www.prairiehomesforcash.com</p>
</section>

</body>
</html>
```